Law Firm Needs a new Website Design

We need a new website design for our law firm located in Manhattan (Law Offices of Branford T. Quellsworth, PLLC).
We have an existing logo that we will to continue using, which can be found in www.QuellsworthLaw.example.
The Peak Counsel, Prime Advocates Logo should also be reflected near the bottom of the Home page.
The website will be 6 pages.

Deliverables:
I want a
1) home page,
2) About Us/Practice Areas page,
3) attorneys,
4) News and Articles page, and
5) Contact and Directions/Privacy Policy page.

The colors of my logo should be in the website.
I also like a touch of black and red.

The website should project "excellence."
We seek to provide the highest quality legal services.
We handle estate planning, wills, trusts, planning for people with disabilities, asset protection and preservation, Medicaid planning, hospital safe discharge, nursing home placement, powers of attorney, health care proxies, living wills, guardianships, probate, estate administration and related litigation.

I would like the colors of my Logo used (including shading where appropriate).
I also want some black on the borders and/or bottom and some red touches throughout the page.

My Logo should appear everywhere that "Law Offices Of Branford T. Quellsworth, PLLC" appears.
I want the badges for Peak counsel, Prime Advocates, Prime Legal Houses, and ZELK on the Home page.
I do not want too much text on the home page.

We would also like the website to have coding.
The final design should also communicate quality, expertise and stability.
Great start so far by the people who submitted designs.
Thank you.

Industry/Entity Type

Law Firm

Coding

Coded - Design and coding required

Number of Pages Required

5+ page

Colors
3276b5
ec1f27
474747

Requirements
Must have
• Please use my logo each time you mention Law Offices of Branford T. Quellsworth, PLLC. Please include the Peakcounsel, Prime Advocates, Prime Legal Houses and Zelk rating Badges on the web home page. I only wish to be contacted by phone. I am not including testimonials and am only using the New York City address.
Nice to have
• Prefer illustrations to photos regarding practice areas
Should not have
• Testimonials, contact me by email, free consultation.

```html
<!DOCTYPE html>
<html lang="en">
<head>
<meta charset="utf-8">
<title>Law Offices of Branford T. Quellsworth, PLLC</title>
<link href="https://fonts.googleapis.com/css2?family=Noto+Serif:wght@400;700&family=Open+Sans:wght@400;600;700&display=swap" rel="stylesheet">
<style>
:root{
  --blue:#3276b5;
  --navy:#262b4f;
  --red:#ec1f27;
  --charcoal:#474747;
  --light:#f1f1f1;
  --ink:#1e1e1e;
  --body:#5a5a5a;
  --muted:#6e6e6e;
  --badge:#c9cdd3;
  --white:#ffffff;
}
*{margin:0;padding:0;box-sizing:border-box}
html,body{width:1200px;height:2214px;overflow:hidden;background:var(--white)}
body{position:relative;font-family:"Open Sans",sans-serif;color:var(--body)}
section,header,nav,footer{position:absolute;left:0;width:1200px}

/* header */
.site-header{top:0;height:103px;background:var(--white)}
.brand{position:absolute;left:77px;top:22px;display:flex;align-items:center;gap:14px}
.brand-mark{width:52px;height:52px;border-radius:50%;background:var(--navy)}
.brand-name{font-family:"Noto Serif",serif;color:var(--blue);font-size:25px;line-height:1.15}
.brand-name small{display:block;font-size:15px}
.call{position:absolute;left:795px;top:20px;display:flex;align-items:center;gap:14px}
.call-icon{width:56px;height:56px;border:2px solid var(--ink);border-radius:50%;display:flex;align-items:center;justify-content:center}
.call-label{font-family:"Noto Serif",serif;font-size:15px;color:var(--ink);letter-spacing:.5px}
.call-number{font-family:"Noto Serif",serif;font-weight:700;font-size:35px;color:var(--red);line-height:1.1}

/* nav */
.main-nav{top:103px;height:52px;background:var(--navy);display:flex;padding-left:77px}
.main-nav a{font-family:"Noto Serif",serif;color:var(--white);text-decoration:none;font-size:19px;line-height:52px;padding:0 23px}
.main-nav a.active{background:var(--blue)}

/* hero */
.hero{top:155px;height:573px;background:linear-gradient(180deg,#f6d3d2 0%,#c7b6cc 38%,#8c8ea3 65%,#6d7b8d 80%,#5d7491 100%)}
.hero-title{position:absolute;right:114px;top:92px;text-align:right;font-family:"Noto Serif",serif;font-weight:400;font-size:41px;line-height:62px;color:var(--ink)}

/* practice */
.practice{top:728px;height:280px;background:var(--light)}
.practice-item{position:absolute;top:-56px;width:240px;text-align:center}
.practice-icon{width:115px;height:115px;margin:0 auto;border-radius:50%;background:var(--blue);display:flex;align-items:center;justify-content:center}
.practice-label{font-family:"Noto Serif",serif;font-size:21px;line-height:31px;color:var(--ink);margin-top:16px}
.btn{position:absolute;background:var(--red);color:var(--white);font-family:"Noto Serif",serif;font-size:20px;text-align:center;border-radius:3px;text-decoration:none}
.btn-view{left:521px;top:161px;width:157px;height:56px;line-height:56px}

/* welcome */
.welcome{top:1008px;height:399px;background:var(--white);text-align:center}
.welcome-mark{position:absolute;left:582px;top:44px;width:36px;height:36px;background:var(--navy);border-radius:50%}
.section-title{font-family:"Noto Serif",serif;color:var(--blue);font-size:43px;font-weight:400}
.welcome .section-title{position:absolute;top:98px;width:100%}
.welcome-text{position:absolute;left:130px;top:172px;width:940px;font-size:15.5px;line-height:25px}
.btn-read{left:514px;top:272px;width:172px;height:56px;line-height:56px}

/* attorneys */
.attorneys{top:1407px;height:364px;background:var(--light)}
.attorneys .section-title{position:absolute;top:42px;width:100%;text-align:center}
.attorney{position:absolute;top:115px;width:510px}
.attorney-photo{position:absolute;left:0;top:0;width:177px;height:177px;border:2px solid var(--blue);padding:5px;background:var(--white)}
.attorney-photo div{width:100%;height:100%}
.attorney-body{position:absolute;left:190px;top:0;width:320px}
.attorney-name{font-family:"Noto Serif",serif;color:var(--blue);font-size:22px;line-height:30px;font-weight:400}
.attorney-bio{font-size:15.5px;line-height:25px;margin-top:2px}
.more{display:inline-block;margin-top:8px;color:var(--red);font-weight:700;font-size:15px;text-decoration:none}

/* recognition */
.recognition{top:1771px;height:171px;background:var(--white)}
.rec-name{position:absolute;top:60px;font-family:"Noto Serif",serif;font-weight:400;font-size:44px;color:var(--muted);line-height:52px}
.rec-peak{left:77px}
.rec-prime{left:465px}
.rec-badge{position:absolute;left:920px;top:40px;width:96px;height:96px;border-radius:8px;background:var(--badge)}

/* footer */
.site-footer{top:1942px;height:219px;background:var(--charcoal);color:var(--white)}
.footer-mark{position:absolute;left:118px;top:36px;width:126px;height:126px;border-radius:50%;background:#8a8a8a}
.footer-col{position:absolute;top:28px}
.footer-col h3{font-family:"Noto Serif",serif;font-weight:400;font-size:22px;margin-bottom:10px}
.footer-col ul{list-style:none}
.links li{font-family:"Noto Serif",serif;font-size:17px;line-height:25px}
.contact li{display:flex;gap:12px;font-size:16px;line-height:24px;margin-bottom:10px}
.contact b{font-weight:700}
.social li{display:flex;align-items:center;gap:18px;font-size:16px;margin-bottom:20px}
.social .dot{width:14px;height:14px;border-radius:50%;background:var(--white)}

.legal-bar{position:absolute;top:2161px;left:0;width:1200px;height:53px;background:var(--red);color:var(--white);text-align:center;line-height:53px;font-size:15.5px}
.legal-bar b{font-weight:700}
</style>
</head>
<body>

<header class="site-header">
  <div class="brand">
    <span class="brand-mark"></span>
    <div class="brand-name"><small>Law Offices of</small>Branford T. Quellsworth, PLLC</div>
  </div>
  <div class="call">
    <span class="call-icon">
      <svg width="26" height="26" viewBox="0 0 24 24"><path fill="#ec1f27" d="M6.6 10.8c1.4 2.8 3.8 5.1 6.6 6.6l2.2-2.2c.3-.3.7-.4 1-.2 1.1.4 2.3.6 3.6.6.6 0 1 .4 1 1V20c0 .6-.4 1-1 1C10.6 21 3 13.4 3 4c0-.6.4-1 1-1h3.5c.6 0 1 .4 1 1 0 1.3.2 2.5.6 3.6.1.3 0 .7-.2 1z"/></svg>
    </span>
    <div>
      <div class="call-label">CALL US NOW!</div>
      <div class="call-number">(212) 555-0148</div>
    </div>
  </div>
</header>

<nav class="main-nav">
  <a class="active" href="#">HOME</a>
  <a href="#">ABOUT / PRACTICE AREA</a>
  <a href="#">ATTORNEY</a>
  <a href="#">NEWS AND ARTICLES</a>
  <a href="#">CONTACT AND DIRECTIONS</a>
</nav>

<section class="hero" role="img" aria-label="Manhattan skyline seen across the harbour at dusk">
  <h1 class="hero-title">QUALITY LEGAL ADVICE &amp;<br>REPRESENTATION</h1>
</section>

<section class="practice">
  <div class="practice-item" style="left:73px">
    <div class="practice-icon">
      <svg width="58" height="58" viewBox="0 0 58 58" fill="none" stroke="#fff" stroke-width="3"><path d="M14 52V22l14-8v38M28 52V6l14 10v36M6 52h46"/><path d="M19 28h4M19 36h4M19 44h4M33 24h4M33 32h4M33 40h4"/></svg>
    </div>
    <div class="practice-label">Estate Planning</div>
  </div>
  <div class="practice-item" style="left:345px">
    <div class="practice-icon">
      <svg width="58" height="58" viewBox="0 0 58 58" fill="none" stroke="#fff" stroke-width="3"><path d="M12 6h24l8 8v38H12z"/><path d="M19 20h18M19 28h18M19 36h10"/><path d="M32 46l16-16 4 4-16 16h-4z"/></svg>
    </div>
    <div class="practice-label">Probate &amp; Estate<br>Administration</div>
  </div>
  <div class="practice-item" style="left:618px">
    <div class="practice-icon">
      <svg width="58" height="58" viewBox="0 0 58 58" fill="#fff"><rect x="20" y="8" width="22" height="12" rx="2" transform="rotate(40 31 14)"/><rect x="10" y="28" width="30" height="5" transform="rotate(-50 25 30)"/><rect x="8" y="46" width="30" height="6" rx="1"/></svg>
    </div>
    <div class="practice-label">Powers of Attorney</div>
  </div>
  <div class="practice-item" style="left:885px">
    <div class="practice-icon">
      <svg width="58" height="58" viewBox="0 0 58 58" fill="none" stroke="#fff" stroke-width="4"><path d="M8 14h16c3 0 5 2 5 5v26c0-3-2-5-5-5H8zM50 14H34c-3 0-5 2-5 5v26c0-3 2-5 5-5h16z"/></svg>
    </div>
    <div class="practice-label">Supplemental Needs<br>Trusts</div>
  </div>
  <a class="btn btn-view" href="#">VIEW ALL</a>
</section>

<section class="welcome">
  <span class="welcome-mark"></span>
  <h2 class="section-title">WELCOME TO BRANFORD T. QUELLSWORTH</h2>
  <p class="welcome-text">Our firm was founded in 1993 by Branford T. Quellsworth, a member of the National Guild of Elder Counsel (NGEC) and an elder law practitioner for over 19 years. Our firm is uniquely positioned to provide quality legal advice and representation in regards to estate planning, wills, trusts, planning for people...</p>
  <a class="btn btn-read" href="#">READ MORE</a>
</section>

<section class="attorneys">
  <h2 class="section-title">OUR ATTORNEYS</h2>
  <article class="attorney" style="left:77px">
    <div class="attorney-photo"><div role="img" aria-label="Portrait of Branford T. Quellsworth in a dark suit" style="background:linear-gradient(160deg,#9cb7cf,#4d5d70)"></div></div>
    <div class="attorney-body">
      <h3 class="attorney-name">Branford T. Quellsworth</h3>
      <p class="attorney-bio">Branford T. Quellsworth was chair of the Metro County Lawyers' Guild pro bono Elder Law Project and the past chair of the Metro County Lawyers' Guild Elder Law Committee.</p>
      <a class="more" href="#">READ MORE &raquo;</a>
    </div>
  </article>
  <article class="attorney" style="left:629px">
    <div class="attorney-photo"><div role="img" aria-label="Portrait of Delphine Harrow Quellsworth in front of bookshelves" style="background:linear-gradient(160deg,#7a5a46,#b58d74 55%,#4f3a30)"></div></div>
    <div class="attorney-body">
      <h3 class="attorney-name">Delphine Harrow Quellsworth</h3>
      <p class="attorney-bio">Delphine Harrow Quellsworth is a graduate of Halvern University and the Whitcombe School of Law where she participated in the Family Law Clinic.</p>
      <a class="more" href="#">READ MORE &raquo;</a>
    </div>
  </article>
</section>

<section class="recognition">
  <div class="rec-name rec-peak">Peak Counsel</div>
  <div class="rec-name rec-prime">Prime Advocates</div>
  <div class="rec-badge" role="img" aria-label="Prime Legal Houses ranking badge"></div>
</section>

<footer class="site-footer">
  <div class="footer-mark"></div>
  <div class="footer-col" style="left:351px">
    <h3>Useful Links</h3>
    <ul class="links"><li>Home</li><li>About</li><li>Attorneys</li><li>News</li><li>Contact</li></ul>
  </div>
  <div class="footer-col" style="left:621px">
    <h3>Get In Touch</h3>
    <ul class="contact">
      <li><svg width="16" height="22" viewBox="0 0 16 22"><path fill="#fff" d="M8 0a8 8 0 0 0-8 8c0 6 8 14 8 14s8-8 8-14a8 8 0 0 0-8-8zm0 11a3 3 0 1 1 0-6 3 3 0 0 1 0 6z"/></svg><span>218 Harlow Avenue, Suite 1407<br>New York, New York 10099</span></li>
      <li><svg width="18" height="18" viewBox="0 0 24 24"><path fill="#fff" d="M6.6 10.8c1.4 2.8 3.8 5.1 6.6 6.6l2.2-2.2c.3-.3.7-.4 1-.2 1.1.4 2.3.6 3.6.6.6 0 1 .4 1 1V20c0 .6-.4 1-1 1C10.6 21 3 13.4 3 4c0-.6.4-1 1-1h3.5c.6 0 1 .4 1 1 0 1.3.2 2.5.6 3.6.1.3 0 .7-.2 1z"/></svg><b>(212) 555-0148</b></li>
      <li><svg width="18" height="18" viewBox="0 0 18 18" fill="none" stroke="#fff" stroke-width="2"><rect x="1" y="5" width="16" height="12" rx="1"/><path d="M5 5V1h8v4M5 10h8M5 13h8"/></svg><span>(212) 555-0193</span></li>
    </ul>
  </div>
  <div class="footer-col" style="left:893px">
    <h3>Follow Us</h3>
    <ul class="social">
      <li><span class="dot"></span>Friendwall</li>
      <li><span class="dot"></span>Chirper</li>
      <li><span class="dot"></span>ProLink</li>
    </ul>
  </div>
</footer>

<div class="legal-bar">&copy; <b>BRANFORD T. QUELLSWORTH</b> - 2016. All Rights Reserved. | Privacy Policy</div>

</body>
</html>
```